Redesign/Facelift for Affiliate Shopping Fashion Site

We are velunix, Fashion web site from Berlin, Germany,
looking to redesign/facelift our affiliate shopping site,
http://shop.velunix.de/bekleidung,27weky56okebmq37,ec_sale,sa
(Main page view)
http://shop.velunix.de/nordwerk-seidentunika-lisel,7uox9m8zsn2bq4j0,i
(Single article view)

Altogether we want to make it more coherent, key words being
MINIMAL and STYLISH.

NOTE:
You don´t need to completely design both pages, it would be sufficient to propose a direction you would take. However, we should be able to envision the complete solution.

The solution should be similar to another comparable affiliate site,
http://www.kaufzimt.de/browse/damen-kleidung

- - General Brief:
The design should have an overall aesthetic coherence,
especially when it comes to sizes of elements
and the bars like in the side bar left, or "Zum Shop".
The solution should be done for the main page and the single article page.

- - Here are the elements in particular, and how they should be designed:
- Main Page HEADER BAR (and single article page) elements:
header bar extends across the entire width of the screen
our logo
"Shopping" text next to the logo
search form
categories "Bekleidung, Accessoires, Schmuck" etc.
Facebook and twitter buttons

- Main page SIDEBAR (left):
elements as can be seen
menu "Preis" is replaced by a price "slider" to more accurately determine
a shopping price range

- Main page PRODUCTS:
elements as can be seen
the "% discount" symbol and "Zum Shop" elements especially
should be looked at

- Main page (and single article page) FOOTER:
should extend across the entire width of the screen

- Single article page
(http://shop.velunix.de/nordwerk-seidentunika-lisel,7uox9m8zsn2bq4j0,i)
header and footer as discussed for the Main page
bars (below the article) "Ähnliche Produkte zu….", "Weitere Produkte…" should be replaced by
"lighter" solution

Thank you,
feel free to ask question if something is not clear.
Kostis

```html
<!DOCTYPE html>
<html lang="de">
<head>
<meta charset="utf-8">
<title>velunix – Bekleidung</title>
<link rel="stylesheet" href="https://fonts.googleapis.com/css2?family=Figtree:wght@400;500;600;700;800&family=Libre+Baskerville&family=Oswald:wght@400;500;700&display=swap">
<style>
:root{
  --accent:#f0424c;
  --dark:#161616;
  --nav:#252525;
  --ink:#1c1c1c;
  --muted:#8a8a8a;
  --line:#dcdcdc;
  --panel:#f4f4f4;
  --white:#ffffff;
}
*{box-sizing:border-box;margin:0;padding:0}
html,body{width:1200px;height:1200px;overflow:hidden;background:var(--white)}
body{font-family:"Figtree",sans-serif;color:var(--ink)}
.stage{position:relative;width:1400px;height:1400px;transform:scale(0.857143);transform-origin:0 0;overflow:hidden}
.abs{position:absolute}
.topline{left:0;top:0;width:1400px;height:4px;background:var(--accent)}
.header{left:0;top:4px;width:1400px;height:116px;background:linear-gradient(#262626,#0f0f0f)}
.logo{left:85px;top:48px;font-size:34px;font-weight:800;color:var(--white);letter-spacing:1px;line-height:40px}
.social{top:32px;width:18px;height:18px;border-radius:50%;background:var(--white)}
.toplinks{right:120px;top:82px;display:flex;font-size:10px;font-weight:600;color:#cfcfcf;letter-spacing:.5px}
.toplinks span{padding:0 11px;border-left:1px solid #555}
.toplinks span:first-child{border-left:none}
.toplinks span:last-child{padding-right:0}
.navbar{left:0;top:120px;width:1400px;height:49px;background:var(--nav)}
.nav{left:85px;top:138px;display:flex;gap:40px;font-size:13px;font-weight:600;letter-spacing:1.3px;color:var(--white)}
.nav .first{font-weight:800}
.nav .more::after{content:"";display:inline-block;margin-left:18px;border:4px solid transparent;border-top:5px solid var(--accent);vertical-align:middle}
.search{left:1056px;top:131px;width:228px;height:29px;background:var(--white);font-size:9px;letter-spacing:.6px;color:#888;padding:10px 20px}
.search svg{position:absolute;right:16px;top:7px}
.side{left:73px;top:201px;width:216px;height:689px;border:1px solid var(--line)}
.shead{position:absolute;left:0;width:214px;height:41px;background:linear-gradient(#fafafa,#e9e9e9);border-bottom:1px solid var(--line);border-top:1px solid var(--line);font-size:13px;font-weight:700;letter-spacing:1px;padding:13px 23px}
.shead .btn{position:absolute;right:28px;top:10px;width:22px;height:22px;border-radius:50%;background:linear-gradient(#fff,#cfcfcf);border:1px solid #bbb}
.shead .btn::after{content:"";position:absolute;left:6px;top:8px;border:4px solid transparent;border-top:5px solid #222}
.shead .btn.r::after{left:8px;top:6px;border:4px solid transparent;border-left:5px solid #222}
.filter{position:absolute;left:12px;font-size:11.5px;width:170px}
.filter b{float:right;font-weight:400}
.item{position:absolute;left:8px;width:176px;height:24px;font-size:12px;letter-spacing:.3px;padding:5px 16px}
.item.on{background:#f1f1f1}
.scroll{position:absolute;left:207px;width:7px;background:#f1f1f1}
.scroll i{display:block;height:52px;background:#dedede}
.crumb{left:326px;top:201px;font-size:12px;color:#555}
.crumb span{color:var(--accent)}
.photo{background:linear-gradient(135deg,#8a7f6e,#3c3a3a 55%,#c9b9a0)}
.hero{left:324px;top:228px;width:663px;height:443px}
.hero-bar{left:324px;top:580px;width:663px;height:91px;background:rgba(20,20,20,.82);color:var(--white)}
.hero-bar h2{position:absolute;left:23px;top:16px;font-size:15px;font-weight:700;letter-spacing:1px}
.hero-bar p{position:absolute;left:22px;top:41px;font-size:12px;line-height:17px;letter-spacing:.4px;width:400px}
.pill{position:absolute;background:var(--accent);color:var(--white);border-radius:17px;font-weight:700;letter-spacing:1px;text-align:center}
.promo{width:316px;overflow:hidden}
.promo .bar{position:absolute;left:0;bottom:0;width:100%;height:60px;background:rgba(25,25,25,.7);color:var(--white);font-size:15px;font-weight:700;letter-spacing:1px;padding:21px 17px}
.promo .bar em{font-style:normal;color:var(--accent);font-size:11px}
.card{top:694px;width:325px;height:216px;border:1px solid var(--line)}
.card .ch{height:44px;background:linear-gradient(#fdfdfd,#ececec);border-bottom:1px solid var(--line);font-family:"Libre Baskerville",serif;font-size:16px;letter-spacing:1px;padding:12px 19px;position:relative}
.card .ch .btn{position:absolute;right:14px;top:10px;width:22px;height:22px;border-radius:50%;background:linear-gradient(#fff,#cfcfcf);border:1px solid #bbb}
.card .ch .btn::after{content:"";position:absolute;left:8px;top:6px;border:4px solid transparent;border-left:5px solid #222}
.thumb{position:absolute;border-radius:6px}
.cta{position:absolute;font-size:13px;color:var(--accent);letter-spacing:.3px;white-space:nowrap}
.cta::after{content:"";display:inline-block;margin-left:9px;border:4px solid transparent;border-left:4px solid var(--accent)}
.rings{left:142px;top:78px;width:172px;text-align:center;font-size:21px;line-height:30px;white-space:nowrap}
.rings b{font-size:22px;font-weight:600;letter-spacing:.2px}
.toolbar{left:323px;top:947px;width:998px;height:50px;background:linear-gradient(#fafafa,#eeeeee);border:1px solid var(--line);border-bottom:2px solid #d4d4d4;font-size:10px;letter-spacing:.5px;color:#555}
.toolbar .sel{position:absolute;left:835px;top:13px;width:145px;height:27px;background:var(--white);border:1px solid #ccc;padding:7px 20px;font-size:10px}
.toolbar .sel i{position:absolute;right:0;top:0;width:30px;height:25px;border-left:1px solid #ccc}
.toolbar .sel i::after{content:"";position:absolute;left:10px;top:10px;border:4px solid transparent;border-top:5px solid #444}
.prod{top:1049px;width:306px;height:360px;border:1px solid #e4e4e4}
.prod .img{position:absolute;left:60px;top:6px;width:186px;height:253px;background:linear-gradient(#f3f3f3,#d9d9d9 60%,#6f6f6f)}
.prod .brand{position:absolute;left:15px;top:284px;font-size:12.5px;color:var(--muted);letter-spacing:1px}
.prod .name{position:absolute;left:15px;top:308px;font-size:12.5px;font-weight:600;letter-spacing:1.3px;white-space:nowrap}
.prod .price{position:absolute;left:15px;top:332px;font-size:14px;color:var(--accent);font-weight:500;word-spacing:2px}
.badge{width:45px;height:45px;border-radius:50%;background:#111;color:var(--white);font-size:12px;font-weight:700;text-align:center;line-height:45px}
</style>
</head>
<body>
<div class="stage">
  <div class="abs topline"></div>
  <header class="abs header"></header>
  <div class="abs logo">VELUNIX</div>
  <div class="abs social" style="left:1176px"></div>
  <div class="abs social" style="left:1216px"></div>
  <div class="abs social" style="left:1254px"></div>
  <nav class="abs toplinks"><span>NEWS</span><span>VELUNIX.TV</span><span>SELECTION</span><span>FASHION ART</span></nav>
  <div class="abs navbar"></div>
  <nav class="abs nav"><span class="first">BEKLEIDUNG</span><span>ACCESSOIRES</span><span>SCHMUCK</span><span>SCHUHE</span><span>TASCHEN</span><span>UHREN</span><span>BEAUTY</span><span>WOHNEN</span><span class="more">MORE</span></nav>
  <div class="abs search">WONACH SUCHST DU?
    <svg width="16" height="16" viewBox="0 0 16 16"><circle cx="6.5" cy="6.5" r="5" fill="none" stroke="#f0424c" stroke-width="2"/><line x1="10" y1="10" x2="14.5" y2="14.5" stroke="#f0424c" stroke-width="2.2"/></svg>
  </div>

  <aside class="abs side">
    <div class="shead" style="top:-1px">KATEGORIEN<span class="btn"></span></div>
    <div class="filter" style="top:55px">Filter Entfernen<b>x</b></div>
    <div class="scroll" style="top:56px;height:238px"><i></i></div>
    <div class="item on" style="top:86px">BEKLEIDUNG (198139)</div>
    <div class="item" style="top:116px">ANZÜGE (139)</div>
    <div class="item" style="top:146px">BADEMODE (4636)</div>
    <div class="item" style="top:176px">BLAZER (968)</div>
    <div class="item" style="top:206px">BLUSEN (2962)</div>
    <div class="item" style="top:236px">WÄSCHE (3501)</div>
    <div class="item" style="top:266px">HEMDEN (7899)</div>
    <div class="shead" style="top:299px">MARKEN<span class="btn"></span></div>
    <div class="filter" style="top:353px">Filter Entfernen<b>x</b></div>
    <div class="scroll" style="top:354px;height:244px"><i></i></div>
    <div class="item on" style="top:384px">BEKLEIDUNG (198139)</div>
    <div class="item" style="top:414px">ANZÜGE (139)</div>
    <div class="item" style="top:444px">BADEMODE (4636)</div>
    <div class="item" style="top:474px">BLAZER (968)</div>
    <div class="item" style="top:504px">BLUSEN (2962)</div>
    <div class="item" style="top:534px">WÄSCHE (3501)</div>
    <div class="item" style="top:564px">HEMDEN (7899)</div>
    <div class="shead" style="top:603px">PREIS<span class="btn r"></span></div>
    <div class="shead" style="top:645px;border-bottom:none">SALE<span class="btn r"></span></div>
  </aside>

  <div class="abs crumb"><span>Start</span> <span>»</span> Bekleidung</div>

  <div class="abs hero photo" role="img" aria-label="Fashion photo of a young couple on a city street"></div>
  <div class="abs hero-bar">
    <h2>LOREM IPSUM</h2>
    <p>Lorem ipsum dolor sit amet, consectetur adipisicing elitsed do eiusmod tempor incididunt ut labore et dolore magna</p>
    <span class="pill" style="left:502px;top:32px;width:123px;height:32px;font-size:12.5px;line-height:32px">LEARN MORE</span>
  </div>

  <div class="abs promo photo" style="left:998px;top:228px;height:222px;background:linear-gradient(135deg,#9aa096,#5b5f5a 50%,#aab0a4)" role="img" aria-label="Photo of a fashion couple in autumn coats">
    <div class="bar">SPECIAL OFFERS <em>›</em></div>
  </div>
  <div class="abs promo photo" style="left:1000px;top:459px;height:210px;background:linear-gradient(135deg,#6a6a6a,#3e4248 50%,#8d8d8d)" role="img" aria-label="Photo of a woman in a denim jacket">
    <div class="bar">SUMER SALE, UP TO 50% OFF <em>›</em></div>
  </div>

  <section class="abs card" style="left:321px">
    <div class="ch">TOP SELLERS<span class="btn"></span></div>
    <div class="thumb" style="left:14px;top:62px;width:106px;height:130px;background:radial-gradient(circle,#f2f2f2,#a9a9a9)" role="img" aria-label="Silver jewel ring"></div>
    <div class="abs" style="left:140px;top:76px;font-family:Oswald,sans-serif;font-size:27px;font-weight:500;letter-spacing:.5px;white-space:nowrap">BACK IN STOCK!</div>
    <div class="abs" style="left:137px;top:112px;width:172px;height:2px;background:#ccc"></div>
    <div class="abs" style="left:136px;top:124px;font-size:13.5px;color:#777;white-space:nowrap">THE BEST JEWEL RINGS</div>
    <span class="cta" style="left:223px;top:190px">SHOP NOW</span>
  </section>
  <section class="abs card" style="left:660px">
    <div class="ch">JEWELLERY<span class="btn"></span></div>
    <div class="thumb" style="left:12px;top:70px;width:124px;height:96px;background:radial-gradient(circle,#e8eef4,#9aa6b0)" role="img" aria-label="Diamond solitaire ring"></div>
    <div class="abs rings">MEET OUR<br><b>BEST-SELLING</b><br>RINGS</div>
    <span class="cta" style="left:163px;top:190px">SHOP BEST SELLERS</span>
  </section>
  <section class="abs card" style="left:999px">
    <div class="ch">OUR PICKS<span class="btn"></span></div>
    <div class="thumb" style="left:10px;top:54px;width:120px;height:140px;background:linear-gradient(135deg,#e7b8c8,#c9d7a8,#b7bfe6)" role="img" aria-label="Pair of floral print slip-on shoes"></div>
    <div class="abs" style="left:241px;top:56px;font-size:24px;line-height:30px">THE</div>
    <div class="abs" style="left:178px;top:82px;font-family:Oswald,sans-serif;font-weight:700;font-size:46px;line-height:52px">COOL</div>
    <div class="abs" style="left:179px;top:142px;font-size:24px">FACTOR</div>
    <span class="cta" style="left:158px;top:190px;color:#f59aa0">SHOP SUMER SHOES</span>
  </section>

  <div class="abs toolbar">
    <span class="abs" style="left:21px;top:20px">SHOWING <b>1-12</b> OF 1350</span>
    <span class="abs" style="left:584px;top:19px;width:13px;height:13px;border:1px solid #bbb;background:#fff"></span>
    <span class="abs" style="left:608px;top:20px">Nur reduzierte Artikel</span>
    <span class="abs" style="left:747px;top:20px">Sortieren nach:</span>
    <div class="sel">BELIEBTESTE<i></i></div>
  </div>

  <article class="abs prod" style="left:320px">
    <div class="img" role="img" aria-label="Product photo: white linen cardigan"></div>
    <span class="brand">CARDINGANS</span>
    <span class="name">MIRELLO CARDIGAN AUS LEINEN, WEIB</span>
    <span class="price">65.00€ &nbsp; € 24.99 €*</span>
  </article>
  <article class="abs prod" style="left:672px">
    <div class="img" style="opacity:.6" role="img" aria-label="Product photo: white linen cardigan"></div>
    <span class="pill" style="left:91px;top:133px;width:123px;height:32px;font-size:12.5px;line-height:32px">VIEW ITEM</span>
    <span class="brand">CARDINGANS</span>
    <span class="name">MIRELLO CARDIGAN AUS LEINEN, WEIB</span>
    <span class="price">65.00€ &nbsp; € 24.99 €*</span>
  </article>
  <article class="abs prod" style="left:1015px">
    <div class="img" role="img" aria-label="Product photo: white linen cardigan"></div>
    <span class="brand">CARDINGANS</span>
    <span class="name">MIRELLO CARDIGAN AUS LEINEN, WEIB</span>
    <span class="price">65.00€ &nbsp; € 24.99 €*</span>
  </article>
  <div class="abs badge" style="left:590px;top:1037px">-31%</div>
  <div class="abs badge" style="left:942px;top:1037px">-45%</div>
  <div class="abs badge" style="left:1285px;top:1037px">-31%</div>
</div>
</body>
</html>
```